Sign Advertisment for Condominium Development

I need a sign created that will be placed in front of a building that is being converted into a luxury condominium development.

The sign needs to say:

Two, Boutique Luxury Condominiums Delivering late 2015.

Luxury Finishes // Designer Kitchens and Bath // Each Unit over 2,000 Square Feet

Deeded Parking Included with Each Unit

To Learn More, Contact:

Marissa Talbot or Vernon Pike
(202) 555-0147
Marissa.Talbot@example-realty.com

I need a small disclaimer at the bottom stating:

These Condominium(s) have not been registered by the Office of Residential Standards and Property Oversight Bureau Tenancy Transition and Transfer Section. A Condominium Unit may be reserved on a non-binding reservation agreement, but no contract of sale or lease that is binding on the purchaser may be entered into prior to registration.

Target Market(s)

Young professionals seeking luxury condominium

Industry/Entity Type

Building

Font styles to use
Serif

Colors
00a88f
ffffff

```html
<!DOCTYPE html>
<html lang="en">
<head>
<meta charset="utf-8">
<title>Boutique Luxury Condominiums Sign</title>
<link rel="stylesheet" href="https://fonts.googleapis.com/css2?family=Bree+Serif&family=Fira+Sans:wght@300;400;600&display=swap">
<style>
  :root {
    --brand-green: #00a88f;
    --paper: #ffffff;
  }
  html, body {
    margin: 0;
    padding: 0;
    width: 1200px;
    height: 800px;
    overflow: hidden;
    background: var(--paper);
  }
  .sign {
    position: relative;
    width: 1200px;
    height: 800px;
    background: var(--paper);
    font-family: "Fira Sans", sans-serif;
    color: var(--paper);
  }
  .sign-panel {
    position: absolute;
    left: 22px;
    top: 22px;
    width: 1156px;
    height: 756px;
    background: var(--brand-green);
  }
  .row {
    position: absolute;
    left: 0;
    width: 100%;
    text-align: center;
    margin: 0;
  }
  .headline {
    top: 68px;
    font-family: "Bree Serif", serif;
    font-weight: 400;
    font-size: 60px;
    line-height: 60px;
    letter-spacing: 0.4px;
    -webkit-text-stroke: 1px var(--paper);
  }
  .headline .count { font-size: 72px; }
  .divider-dots {
    display: flex;
    justify-content: center;
    gap: 22px;
  }
  .divider-dots span {
    width: 8px;
    height: 8px;
    border-radius: 50%;
    background: var(--paper);
  }
  .dots-top { top: 230px; }
  .dots-bottom { top: 418px; }
  .features {
    top: 251px;
    list-style: none;
    padding: 0;
    font-weight: 600;
    font-size: 30px;
    line-height: 37.5px;
  }
  .features .light { font-weight: 400; }
  .contact-intro {
    top: 449px;
    font-weight: 300;
    font-size: 27px;
  }
  .contact-names {
    top: 492px;
    font-size: 28px;
    font-weight: 400;
    display: flex;
    justify-content: center;
    align-items: center;
    gap: 10px;
  }
  .contact-names strong { font-weight: 600; }
  .contact-lines {
    top: 534px;
    font-size: 28px;
    font-weight: 400;
    display: flex;
    justify-content: center;
    align-items: center;
    gap: 32px;
  }
  .contact-item {
    display: flex;
    align-items: center;
    gap: 14px;
  }
  .icon { display: block; fill: var(--paper); }
  .partners {
    top: 626px;
    display: flex;
    justify-content: center;
    gap: 100px;
    font-weight: 600;
    font-size: 20px;
  }
  .partner-name {
    display: flex;
    align-items: center;
    gap: 8px;
  }
  .partner-mark {
    width: 12px;
    height: 12px;
    background: var(--paper);
  }
  .disclaimer {
    top: 683px;
    left: 150px;
    width: 856px;
    font-weight: 300;
    font-size: 13px;
    line-height: 18px;
  }
</style>
</head>
<body>
<div class="sign">
  <div class="sign-panel">
    <h1 class="row headline"><span class="count">2</span> Boutique Luxury Condominiums<br>Delivering late 2015.</h1>

    <div class="row divider-dots dots-top"><span></span><span></span><span></span></div>

    <ul class="row features">
      <li>Luxury Finishes</li>
      <li>Designer Kitchens and Bath</li>
      <li>Each Unit over <span class="light">2,000 Square Feet</span></li>
      <li>Deeded Parking Included with Each Unit</li>
    </ul>

    <div class="row divider-dots dots-bottom"><span></span><span></span><span></span></div>

    <p class="row contact-intro">To Learn More, Contact:</p>

    <p class="row contact-names">
      <svg class="icon" width="26" height="24" viewBox="0 0 26 24" aria-hidden="true">
        <circle cx="13" cy="7" r="6"/>
        <path d="M1 24c0-7 5-10 12-10s12 3 12 10z"/>
      </svg>
      <span><strong>Marissa Talbot</strong> or <strong>Vernon Pike</strong></span>
    </p>

    <p class="row contact-lines">
      <span class="contact-item">
        <svg class="icon" width="18" height="22" viewBox="0 0 18 22" aria-hidden="true">
          <path d="M4 1l3 5-2 2c1 3 3 6 6 8l2-2 4 3-2 4C8 21 1 12 1 4z"/>
        </svg>
        (202) 555-0147
      </span>
      <span class="contact-item">
        <svg class="icon" width="26" height="18" viewBox="0 0 26 18" aria-hidden="true">
          <path d="M0 0h26v2L13 10 0 2z"/>
          <path d="M0 5l13 8 13-8v13H0z"/>
        </svg>
        Marissa.Talbot@example-realty.com
      </span>
    </p>

    <div class="row partners">
      <span class="partner-name"><span class="partner-mark"></span>Halvorsen Builders</span>
      <span class="partner-name">Capitol Row Properties</span>
      <span class="partner-name"><span class="partner-mark"></span>Quillmere Savings Trust</span>
    </div>

    <p class="row disclaimer">These Condominium(s) have not been registered by the Office of Residential Standards and Property Oversight Bureau Tenancy Transition and Transfer Section. A Condominium Unit may be reserved on a non-binding reservation agreement, but no contract of sale or lease that is binding on the purchaser may be entered into prior to registration.</p>
  </div>
</div>
</body>
</html>
```